Football (Soccer) Themed Beer Can

We need a package deisgn created for a beer can. The are two attachments. One is additional brief information. The other shows a range or existing competitive cans for inspiration.

More than anything, the designs should be green, white and FUN. The brand is and must clearly be TOLVANBREW. We need something that is fun enough to demand attention on shelf. It should also be clean enough to appeal to Scandinavian taste but a little humor is OK. The brand must ben fun and have some personality.

The designs are for a beer brand called TOLVANBREW based on the soccer team called Sjöholmen. The base colors must be green and white. The attached document shows those colors and different team executions. The beer could follow an existing execution (such as a shirt) or it could have an all new green and white concept. The name TOLVANBREW should be very visible in the block font that we show in the attachment. There is also a logo in the attachment which shows the team logo - a green and white flag inside a circular yellow wheat element. This logo could be somewhere in the design but it is not required. If used, the flag should read TBW instead of the existing SIK.

There are also a few text elements in the attached document. They should be included somewhere. They need not be obvious. They could be sneaked into the design so that people would have to find them. That could be part of the fun - having semi hidden messages that mean something to the team's fans.

Ultimately, the design will have to executed on a green bottle as well. That would be helpful but is not required of this project.

Target Market(s)

Nordic Men aged 18-60

Industry/Entity Type

Beer

Font styles to use
Sans Serif
Script
Other font styles liked:
• The main logo is sans serit, some accents can be script.

Colors
00AB8E
00BBA5
67D7C9
C6EFE9
E9F9F6

Requirements
Must have
• Name TOLVANBREW
Nice to have
• Make is classy looking yet fun
Should not have
• It should not scream football. It should be a nice stand-alone look.

```html
<!DOCTYPE html>
<html lang="sv">
<head>
<meta charset="utf-8">
<title>TOLVANBREW – label designs</title>
<link rel="stylesheet" href="https://fonts.googleapis.com/css2?family=Roboto:wght@500;700&family=Roboto+Condensed:wght@500&family=Caveat:wght@400&display=swap">
<style>
  :root {
    --page: #f2f2f2;
    --label-green: #2f9350;
    --label-deep: #1f7a3d;
    --label-light: #5cbf78;
    --pattern-dark: #236e3a;
    --ink-white: #ffffff;
    --ink-soft: rgba(255, 255, 255, 0.85);
    --script-soft: rgba(170, 225, 185, 0.55);
  }
  * { margin: 0; padding: 0; box-sizing: border-box; }
  html, body { width: 1200px; height: 900px; overflow: hidden; }
  body {
    background: var(--page);
    display: flex;
    justify-content: center;
    align-items: center;
    gap: 150px;
  }
  .label {
    position: relative;
    width: 300px;
    height: 640px;
    background: linear-gradient(90deg, var(--label-deep) 0%, var(--label-green) 30%, var(--label-green) 70%, var(--label-deep) 100%);
    border-radius: 6px;
    overflow: hidden;
    color: var(--ink-white);
  }
  .label__pattern {
    position: absolute;
    left: 0; right: 0; top: 0;
    background: linear-gradient(160deg, var(--label-light) 0%, var(--label-green) 40%, var(--pattern-dark) 70%, var(--label-green) 100%);
    opacity: 0.85;
  }
  .label--lower .label__pattern { height: 63%; }
  .label--upper .label__pattern { height: 88%; }
  .wordmark {
    position: absolute;
    writing-mode: vertical-rl;
    font-family: "Roboto", Arial, sans-serif;
    font-weight: 700;
    color: var(--ink-white);
    line-height: 1;
  }
  .label--lower .wordmark {
    left: 106px; top: 40px;
    font-size: 76px;
    letter-spacing: -2px;
    text-transform: lowercase;
  }
  .label--upper .wordmark {
    left: 112px; top: 0;
    font-size: 72px;
    letter-spacing: -1px;
    text-transform: uppercase;
    color: rgba(255, 255, 255, 0.88);
  }
  .tagline {
    position: absolute;
    left: 0; right: 0;
    font-family: "Roboto Condensed", Arial, sans-serif;
    font-weight: 500;
    text-align: center;
    color: var(--ink-soft);
  }
  .label--lower .tagline { bottom: 60px; font-size: 13px; line-height: 1.45; padding: 0 78px; }
  .label--upper .tagline { bottom: 18px; font-size: 11px; line-height: 1.4; padding: 0 70px; }
  .facts {
    position: absolute;
    bottom: 22px;
    font-family: "Roboto Condensed", Arial, sans-serif;
    font-size: 12px;
    line-height: 1.4;
    text-align: center;
    color: var(--ink-soft);
  }
  .facts--abv { left: 30px; }
  .facts--volume { right: 40px; }
  .script-note {
    position: absolute;
    font-family: "Caveat", cursive;
    font-size: 17px;
    color: var(--script-soft);
    white-space: nowrap;
  }
  .script-note--top { left: 28px; top: 34px; transform: rotate(-14deg); }
  .script-note--left { left: 2px; bottom: 50px; transform: rotate(-62deg); font-size: 14px; }
  .script-note--right { right: -24px; bottom: 60px; transform: rotate(64deg); font-size: 14px; }
</style>
</head>
<body>
  <section class="label label--lower" aria-label="TOLVANBREW label, lowercase version">
    <div class="label__pattern" role="img" aria-label="Collage pattern of layered green club graphics"></div>
    <p class="script-note script-note--top">så är jag stark öl</p>
    <h1 class="wordmark">tolvanbrew</h1>
    <p class="tagline">Lorem ipsum dolor sit amet, consectetuer adipi-scing elit,</p>
    <p class="facts facts--abv">5,2%<br>alc</p>
    <p class="facts facts--volume">500<br>ml</p>
  </section>

  <section class="label label--upper" aria-label="TOLVANBREW label, uppercase version">
    <div class="label__pattern" role="img" aria-label="Collage pattern of layered green club graphics"></div>
    <h2 class="wordmark">TOLVANBREW</h2>
    <p class="script-note script-note--left">Hej jag är stark öl</p>
    <p class="script-note script-note--right">Heja heja heja</p>
    <p class="tagline">Lorem ipsum dolor sit amet, consectetuer adipiscing elit,</p>
  </section>
</body>
</html>
```